Book cover: Muddling Through Small Years (A5)

I have a book called Muddling Through Big Years. It is a book for teenagers which gives them tips and tactics on how to survive life's challenges regarding friends, family, feelings, relationships and hard stuff in life generally. I will upload the cover of this book but you can see it on my past jobs as one of the designers her eon Pixel Harbor did it for me.
I have a new book I've written called Muddling Through Small Years. This is a parallel book to Muddling Through Big Years, but it is specifically for 8 to 12 or 13 year olds, rather than for older teens.
A very important aspect of this job is that it SHOULD MATCH in some strong way - the Muddling Through Big Years book. I will be selling them together, displaying them together and I want them to look like two of a pair. It might be that you use the same image as the first book but change the colour of the image so that it is bright orange and green perhaps? Or that there is another image but in the image is placed in the exact same position across the book as the first book. It needs to look like the books are by the same author.
However, I would like this one to look a bit "younger", more kid friendly. For example, a font that looks like it is for kids, or kids' writing perhaps.
I dont want to have photos on the book, and I dont think I want cartoons or drawings - because I'm not sure how this will tie in with the first book.
I want it to look modern, fresh and designed specifically for kids. The text needs to be:
Muddling Through - Small Years!
Tips and ideas for 8 to 13 year olds about how to stay cool, calm and confident on even the toughest days!
The back cover is going to mostly just have the table of contents listed and a blurb, with one or two cartoons which I will supply. I am keen to pick a designer to just do the front cover first and will ask them to do the back cover later.
UPDATED: I have attached three files with fonts that I like.

```html
<!DOCTYPE html>
<html lang="en">
<head>
<meta charset="utf-8">
<title>Muddling Through Small Years — Book Cover</title>
<link rel="stylesheet" href="https://fonts.googleapis.com/css2?family=Covered+By+Your+Grace&family=Gochi+Hand&family=Open+Sans:wght@400&display=swap">
<style>
  :root {
    --paper: #ffffff;
    --ink: #1a1a1a;
    --accent-orange: #f0962a;
    --art-light: #f9bb55;
    --art-mid: #ee9526;
    --art-deep: #b8650f;
    --art-turquoise: #22e0d6;
    --art-turquoise-deep: #12b3ad;
  }
  html, body {
    margin: 0;
    padding: 0;
    width: 800px;
    height: 1200px;
    overflow: hidden;
    background: var(--paper);
  }
  .cover {
    position: relative;
    width: 800px;
    height: 1200px;
    background: var(--paper);
    overflow: hidden;
    color: var(--ink);
  }
  .title-small {
    position: absolute;
    left: 106px;
    top: 104px;
    margin: 0;
    font-family: "Covered By Your Grace", cursive;
    font-size: 60px;
    line-height: 1;
    letter-spacing: 3px;
    font-weight: 400;
  }
  .title-big {
    position: absolute;
    left: 104px;
    top: 165px;
    margin: 0;
    font-family: "Covered By Your Grace", cursive;
    font-size: 112px;
    line-height: 1;
    letter-spacing: 34px;
    font-weight: 400;
    white-space: nowrap;
  }
  .title-tag {
    position: absolute;
    left: 414px;
    top: 80px;
    margin: 0;
    font-family: "Gochi Hand", cursive;
    font-size: 64px;
    line-height: 1;
    color: var(--accent-orange);
    transform: rotate(-6deg);
    transform-origin: left center;
    font-weight: 400;
    white-space: nowrap;
  }
  .subtitle {
    position: absolute;
    left: 110px;
    top: 282px;
    width: 670px;
    margin: 0;
    font-family: "Open Sans", sans-serif;
    font-size: 21px;
    line-height: 32px;
    color: #222222;
  }
  .cover-art {
    position: absolute;
    left: 0;
    top: 385px;
    width: 800px;
    height: 530px;
    background:
      radial-gradient(circle at 27% 50%, var(--art-turquoise) 0%, var(--art-turquoise-deep) 16%, rgba(18, 179, 173, 0) 26%),
      radial-gradient(circle at 60% 30%, rgba(255, 210, 120, 0.55) 0%, rgba(255, 210, 120, 0) 22%),
      radial-gradient(circle at 80% 75%, rgba(255, 200, 110, 0.5) 0%, rgba(255, 200, 110, 0) 25%),
      radial-gradient(ellipse at 45% 40%, var(--art-light) 0%, var(--art-mid) 55%, var(--art-deep) 100%);
  }
  .author {
    position: absolute;
    left: 370px;
    top: 1030px;
    width: 380px;
    text-align: center;
  }
  .author-name {
    margin: 0;
    font-family: "Covered By Your Grace", cursive;
    font-size: 50px;
    line-height: 1;
    letter-spacing: 1px;
    text-transform: uppercase;
    font-weight: 400;
  }
  .author-role {
    margin: 14px 0 0;
    font-family: "Open Sans", sans-serif;
    font-size: 26px;
    line-height: 1.2;
  }
</style>
</head>
<body>
  <main class="cover">
    <header class="cover-title">
      <h1 class="title-small">MUDDLING</h1>
      <p class="title-big">THROUGH</p>
      <p class="title-tag">Small Years</p>
    </header>
    <p class="subtitle">tips and ideas for 8 to 13 year olds about how to stay cool,<br>calm and confident on even the toughest days!</p>
    <div class="cover-art" role="img" aria-label="A crowd of glossy orange smiley balls surrounding one turquoise ball with a sad expression"></div>
    <footer class="author">
      <p class="author-name">Rosalind Pell</p>
      <p class="author-role">clinical psychologist</p>
    </footer>
  </main>
</body>
</html>
```